Auto Body Shops Needs Email Signature Design

We are looking to update our email signature. The design needs to be easy to copy and paste into Microsoft Outlook and be editable for multiple positions.

Our company is called Velnor Collision & Autoglass, but we have a charity program called Velnor Helps the Young. We would like to use this logo.

Information that needs to be included:

"We Care"
Name
Title
Location
Address
Phone
Email
Cell
Fax

Our new corporate colors are gray/silver and black. We are getting away from blue (currently used).

The "Velnor" and "Helps the" should be in black as they will be on a white background (comp screen).

Colors
fde1e1

Requirements
Must have
• Easily editable so it can be used as a template.
Should not have
• Main color should not be red.

```html
<!DOCTYPE html>
<html lang="en">
<head>
<meta charset="utf-8">
<title>Velnor Email Signature</title>
<link href="https://fonts.googleapis.com/css2?family=Carlito:wght@400;700&family=Didact+Gothic&display=swap" rel="stylesheet">
<style>
  :root {
    --paper: #ffffff;
    --ink: #1a1a1a;
    --soft-gray: #8a8a8a;
    --name-gray: #767676;
    --accent-red: #e0383d;
    --link-red: #e0383d;
    --blush: #fde1e1;
  }
  * { margin: 0; padding: 0; box-sizing: border-box; }
  html, body {
    width: 1200px;
    height: 651px;
    overflow: hidden;
    background: var(--paper);
  }
  .message {
    width: 1200px;
    height: 651px;
    padding: 34px 24px 0 24px;
    color: var(--ink);
    font-family: "Carlito", "Calibri", sans-serif;
    font-size: 14px;
    line-height: 18px;
  }
  .message p { margin-bottom: 18px; }
  .signature {
    font-family: "Didact Gothic", "Century Gothic", sans-serif;
    margin-top: 6px;
  }
  .tagline {
    color: var(--soft-gray);
    font-size: 17px;
    line-height: 22px;
    padding-bottom: 9px;
    width: 136px;
    border-bottom: 2px solid var(--accent-red);
  }
  .person-name {
    margin-top: 10px;
    color: var(--name-gray);
    font-size: 18px;
    font-weight: 700;
    line-height: 20px;
    font-family: "Carlito", "Calibri", sans-serif;
  }
  .person-role {
    font-size: 15px;
    line-height: 20px;
    color: var(--ink);
  }
  .person-role .location { font-size: 13px; }
  .person-role .divider { margin: 0 5px; }
  .person-role a, .site-link { color: var(--link-red); text-decoration: underline; }
  .contact-lines { margin-top: 8px; font-size: 12.5px; line-height: 19px; }
  .contact-line { display: flex; align-items: center; gap: 8px; }
  .contact-line svg { width: 10px; height: 11px; flex: none; }
  .program-name {
    display: flex;
    align-items: center;
    gap: 6px;
    margin-top: 4px;
    margin-left: 8px;
    height: 30px;
    font-size: 17px;
    line-height: 30px;
    color: var(--ink);
  }
  .program-name .mark {
    width: 10px; height: 10px; border-radius: 50%;
    background: var(--accent-red);
  }
  .site-link { display: inline-block; font-size: 12.5px; margin-top: 2px; }
  .disclaimer {
    margin-top: 18px;
    font-size: 9.2px;
    line-height: 13px;
    color: var(--ink);
    max-width: 1150px;
  }
</style>
</head>
<body>
<main class="message">
  <p class="greeting">Dear Sirs,</p>
  <p>Sit at reque vivendum, mea minim admodum id, vim quis idque homero ei. Case ipsum qualisque et eum, ad sit iuvaret deleniti signiferumque, modus semper ornatus an sea. Vis erant propriae ex. Exerci singulis te mei, ei eros sonet has, quo an case libris quaestio. Ex graece aliquando ius, cum mucius concludaturque ad, ad sed noster prompta mandamus.</p>
  <p>Cu sit falli singulis partiendo, porro graeci putant vix an, in dicta convenire est. Et melius accumsan mea, adhuc deterruisset ut duo, cu mea dictas invidunt. No expetendis neglegentur sea. Usu nulla petentium accommodare ad.</p>

  <section class="signature">
    <div class="tagline">We Care</div>
    <div class="person-name">Your Name</div>
    <div class="person-role">Regional Manager<span class="divider">|</span><span class="location">H.O. Brenford</span><span class="divider">|</span><a href="mailto:email@velnor.com">email@velnor.com</a></div>

    <div class="contact-lines">
      <div class="contact-line">
        <svg viewBox="0 0 10 11" aria-hidden="true"><path d="M2 0h6l1 3-2 1v3l2 1-1 3H2L1 8l2-1V4L1 3z" fill="#e0383d"/></svg>
        <span>604-555-0147</span>
      </div>
      <div class="contact-line">
        <svg viewBox="0 0 10 11" aria-hidden="true"><rect x="2" y="1" width="6" height="4" fill="#e0383d"/><rect x="0" y="4" width="10" height="5" rx="1" fill="#e0383d"/><rect x="2.5" y="7" width="5" height="3" fill="#fff"/></svg>
        <span>604-555-0147</span>
      </div>
    </div>

    <div class="program-name"><span class="mark"></span><span>Velnor Helps the Young</span></div>
    <a class="site-link" href="http://www.velnor.com/">http://www.velnor.com/</a>

    <p class="disclaimer">This e-mail and any attachments may contain confidential information. It is intended for the addressee(s) names herein. If you are not the intended recipient of this e-mail you are notified that any dissemination, distribution or duplication of this email and attachments is strictly prohibited. If you received this e-mail in error, please notify me immediately and permanently delete / dispose of the original and any copy of the email, attachments or printed copies.</p>
  </section>
</main>
</body>
</html>
```